Prepared ready to cook meal delivery service needs a flyer design

We need a flyer design for a startup company based in Cape Town, South Africa. I've attached a few flyer designs that I like.

The company is called 'Brindle' and our website will be found at brindle.co.za. We don't have a logo yet.

Flyer text:

Brindle
Ready to roast

Do you feel like a home cooked meal but don't like shopping, peeling, chopping, cooking, or cleaning up?

We deliver ready to roast free range chicken and fresh vegetables to your door.

To order: SMS your name to 083 614 2958 and we'll call you back.

Only the best ingredients used
Free range chickens. Fresh herbs and vegetables. Virgin olive oil.

No bad carbs!

Ready to roast Free range chicken and fresh veggies
For 2 R99
For 4 R139
Updates

Wording of flyer updated.

Target Market(s)

Local Cape Townians that hate grocery shopping and need help saving time preparing meals.

Industry/Entity Type

Delivery Service

Requirements
Must have
• To find out more: SMS your name to 083 614 2958

```html
<!DOCTYPE html>
<html lang="en">
<head>
<meta charset="utf-8">
<title>Brindle – Ready to Roast Flyer</title>
<link href="https://fonts.googleapis.com/css2?family=Oswald:wght@500;700&family=Roboto+Condensed:ital,wght@0,700;1,700&family=Arimo:wght@400;700&display=swap" rel="stylesheet">
<style>
  :root {
    --cream: #f8ecd6;
    --cream-light: #fdf8ee;
    --gold: #c49a4f;
    --gold-band: #c8a25e;
    --brown-dark: #3e3427;
    --ink: #2f271d;
    --white: #ffffff;
    --photo-warm: #c98a3e;
    --photo-deep: #8a4f1e;
    --photo-plate: #f3ede4;
  }
  * { margin: 0; padding: 0; box-sizing: border-box; }
  html, body { width: 898px; height: 1200px; overflow: hidden; }
  body { background: var(--cream-light); font-family: "Arimo", Arial, sans-serif; color: var(--ink); }

  .flyer {
    position: relative; width: 898px; height: 1200px; overflow: hidden;
    background: radial-gradient(ellipse at 50% 35%, var(--cream-light) 0%, var(--cream) 70%);
  }
  .top-tagline {
    position: absolute; top: 28px; width: 100%; text-align: center;
    font-size: 25px; color: var(--ink);
  }
  .top-tagline .accent { color: var(--gold); }

  .brand {
    position: absolute; top: 100px; left: 0; width: 100%;
    display: flex; align-items: center; justify-content: center; gap: 34px;
  }
  .brand-dot { width: 120px; height: 120px; border-radius: 50%; background: var(--gold); }
  .brand-text { display: flex; flex-direction: column; }
  .brand-name {
    font-family: "Oswald", sans-serif; font-weight: 700; font-size: 96px;
    line-height: 1; color: var(--brown-dark); letter-spacing: 4px;
  }
  .brand-line {
    font-family: "Oswald", sans-serif; font-weight: 500; font-size: 44px;
    line-height: 1.1; color: var(--brown-dark); letter-spacing: 1px;
  }

  .band-dark {
    position: absolute; top: 282px; left: 0; width: 100%; height: 86px;
    background: var(--brown-dark); display: flex; align-items: center; justify-content: center;
    font-family: "Roboto Condensed", sans-serif; font-style: italic; font-weight: 700;
    color: var(--white); font-size: 38px; letter-spacing: 1px; gap: 12px;
  }
  .band-dark .highlight { color: var(--gold); font-size: 50px; }

  .band-gold {
    position: absolute; top: 368px; left: 0; width: 100%; height: 96px;
    background: var(--gold-band); text-align: center; padding-top: 12px;
    font-family: "Roboto Condensed", sans-serif; font-style: italic; font-weight: 700;
    font-size: 31px; line-height: 1.3; color: var(--ink);
  }

  .offer {
    position: absolute; top: 510px; left: 60px; width: 460px; text-align: center;
    font-size: 27px; line-height: 1.4; font-weight: 700; color: var(--ink);
  }
  .offer .accent { color: var(--gold); }
  .prices {
    position: absolute; top: 640px; left: 92px;
    font-family: "Roboto Condensed", sans-serif; font-weight: 700; font-size: 31px; color: var(--ink);
  }
  .prices .amount { color: var(--gold); font-size: 42px; margin-right: 18px; }

  .photo {
    position: absolute; top: 735px; left: 0; width: 100%; height: 360px;
    background:
      radial-gradient(ellipse 34% 46% at 48% 52%, var(--photo-warm) 0%, var(--photo-deep) 60%, transparent 100%),
      radial-gradient(ellipse 60% 40% at 55% 75%, var(--photo-plate) 0%, transparent 100%),
      linear-gradient(180deg, var(--cream) 0%, var(--photo-plate) 100%);
  }

  .sms-badge { position: absolute; top: 490px; left: 476px; width: 340px; height: 340px; }

  .quality {
    position: absolute; top: 1090px; width: 100%; text-align: center;
    font-family: "Roboto Condensed", sans-serif; font-style: italic; font-weight: 700; color: var(--ink);
  }
  .quality-head { font-size: 40px; line-height: 1.1; }
  .quality-list { font-size: 19px; margin-top: 6px; }
</style>
</head>
<body>
  <main class="flyer">
    <p class="top-tagline">Ready to roast <span class="accent">Free range chicken and fresh veggies</span></p>

    <header class="brand">
      <span class="brand-dot"></span>
      <div class="brand-text">
        <span class="brand-name">BRINDLE</span>
        <span class="brand-line">READY TO ROAST</span>
      </div>
    </header>

    <div class="band-dark">FEEL LIKE A <span class="highlight">HOME COOKED MEAL?</span></div>
    <div class="band-gold">Don't like shopping, peeling, chopping,<br>cooking, or cleaning up?</div>

    <p class="offer">We deliver <span class="accent">ready to roast</span><br>free range chicken and fresh<br>vegetables <span class="accent">to your door.</span></p>
    <p class="prices">For 2 <span class="amount">R99</span>For 4 <span class="amount">R139</span></p>

    <div class="photo" role="img" aria-label="Golden roast chicken with roast potatoes and fresh herbs on a white plate"></div>

    <svg class="sms-badge" viewBox="0 0 340 340" aria-label="SMS your name to 083 614 2958, we'll call you back">
      <defs>
        <path id="call-back-arc" d="M 138 41 A 142 142 0 0 1 272 272" fill="none"/>
      </defs>
      <circle cx="163" cy="181" r="128" fill="var(--brown-dark)"/>
      <text font-family="Oswald, sans-serif" font-weight="700" font-size="23" fill="var(--ink)" letter-spacing="2">
        <textPath href="#call-back-arc" startOffset="0">WE'LL CALL YOU BACK</textPath>
      </text>
      <text x="163" y="180" text-anchor="middle" font-family="Oswald, sans-serif" font-weight="700" font-size="74" fill="var(--gold)">SMS</text>
      <text x="163" y="224" text-anchor="middle" font-family="Oswald, sans-serif" font-weight="500" font-size="34" fill="var(--white)">YOUR NAME</text>
      <line x1="60" y1="242" x2="266" y2="242" stroke="var(--gold)" stroke-width="2"/>
      <text x="163" y="278" text-anchor="middle" font-family="Arimo, sans-serif" font-size="26" fill="var(--white)">083 614 2958</text>
    </svg>

    <footer class="quality">
      <p class="quality-head">Only the best ingredients used</p>
      <p class="quality-list">Free range chickens. Fresh herbs and vegetables. Virgin olive oil.</p>
    </footer>
  </main>
</body>
</html>
```